Small Business Marketing Workflow

BloomNest is Small Business Marketing made simple.
We built BloomNest to be a place where small businesses can find the tools and expertise to transform their marketing efforts help their businesses to Thrive. We provide a integrated platform where they can create emails, postcards, social media, mobile ads and measure their effectiveness- all right from the platform.

We have a defined look and feel that is helpful, friendly and approachable yet professional. We target the small business owner who may not be marketing or tech savvy.

We need to design the workflow page for building a marketing activity (email, postcard etc..) which outlines a series of steps which the user must go through to complete the task. It should guide the user through the process in an intuitive, clear and simple way yet keeping our brand personality / icons present.

We want the design to keep to our template of colors (yellows, orange etc..) and brand icons in the page design.

Our homepage is www.bloomnest-example.com and we are attached product screens.
Updates

As a further clarification:

The design needs to fit into the Product pages (not the website) I have uploaded the pages for you to what the product looks like.

Target Market(s)

Small Business Owners who are not marketing or tech-savvy

Industry/Entity Type

Small Business

Requirements
Must have
• For your design please take one marketing activity, Build an Email and design the steps
1) Get started
2)Choose Template
3)Edit Email
4) Select your send to list
5) Schedule

Also, the design must show the user which step they are on and allow them to navigate back and forth between steps, saves their drafts, and offers them helpful tips along the way.

```html
<!DOCTYPE html>
<html lang="en">
<head>
<meta charset="utf-8">
<title>BloomNest – Build an Email</title>
<link href="https://fonts.googleapis.com/css2?family=Arimo:wght@400;700&display=swap" rel="stylesheet">
<style>
  :root {
    --orange: #f57a12;
    --orange-deep: #ee6a05;
    --orange-light: #ffa640;
    --yellow: #ffd84a;
    --yellow-pale: #ffeaa0;
    --page: #f3f3f3;
    --card: #ffffff;
    --line: #d6d6d6;
    --text: #333333;
    --muted: #7a7a7a;
    --faint: #9a9a9a;
    --dark-btn: #2b2b2b;
  }
  * { box-sizing: border-box; margin: 0; padding: 0; }
  html, body { width: 924px; height: 1200px; overflow: hidden; }
  body {
    position: relative;
    font-family: "Arimo", Arial, sans-serif;
    color: var(--text);
    background: linear-gradient(#ffffff 0, #f1f1f1 40px, #ffffff 300px, #f7f7f7 600px, #f4f4f4 1120px, #e9e9e9 1200px);
  }
  .abs { position: absolute; }

  /* top bar */
  .brand-name {
    left: 40px; top: 14px;
    font-size: 46px; font-weight: 700; letter-spacing: -1px;
    color: var(--orange-light);
  }
  .user-bar {
    left: 680px; top: 0; width: 190px; height: 35px;
    background: linear-gradient(#ffffff, #ececec);
    border: 1px solid #d8d8d8; border-top: none;
    border-radius: 0 0 6px 6px;
    box-shadow: 0 2px 3px rgba(0,0,0,.15);
    font-size: 11.5px; color: #444;
    display: flex; align-items: center; justify-content: center; gap: 12px;
  }

  /* header band */
  .header-band {
    left: 0; top: 76px; width: 924px; height: 224px;
    background: linear-gradient(#ff9a2a 0, #f78016 50%, #f26f0a 100%);
  }
  .header-band::before {
    content: ""; position: absolute; left: 0; top: 0; width: 100%; height: 4px;
    background: #ffb04a;
  }
  .business-tab {
    left: 680px; top: 76px; width: 191px; height: 40px;
    background: linear-gradient(#ffffff, #e9e9e9);
    border-radius: 0 0 4px 4px;
    box-shadow: 0 2px 3px rgba(0,0,0,.2);
    font-size: 12px; color: #444;
    display: flex; align-items: center; justify-content: center;
  }
  .logo-card {
    left: 60px; top: 135px; width: 298px; height: 138px;
    background: var(--card);
    border: 3px solid var(--yellow);
    border-radius: 6px;
    display: flex; align-items: center; justify-content: center; gap: 12px;
  }
  .logo-card .mark { width: 30px; height: 30px; border-radius: 50%; background: var(--yellow); }
  .logo-card .name { font-size: 28px; font-weight: 700; color: #6b3d12; }

  .main-nav {
    left: 421px; top: 135px; width: 447px; height: 138px;
    background: linear-gradient(#ffe78a, #ffd84a);
    border: 3px solid #ffcf3a;
    border-radius: 6px;
  }
  .nav-btn {
    position: absolute; width: 175px; height: 44px;
    background: linear-gradient(#4a4a4a, #1e1e1e);
    border-radius: 5px;
    box-shadow: 0 2px 3px rgba(0,0,0,.35);
    color: #fff; font-size: 13px;
    display: flex; align-items: center; gap: 8px; padding-left: 14px;
  }
  .nav-btn svg { width: 17px; height: 17px; }

  /* tabs */
  .tab {
    top: 347px; width: 123px; height: 39px;
    background: linear-gradient(#ffffff, #ececec);
    border: 1px solid #cfcfcf; border-bottom: none;
    border-radius: 5px 5px 0 0;
    font-size: 17px; color: #333;
    display: flex; align-items: center; justify-content: center;
  }
  .tab.is-active {
    background: linear-gradient(90deg, #ffc425, #ff8a12);
    border-color: #f0a020;
    justify-content: flex-start; padding-left: 40px;
  }

  .workflow-panel {
    left: 32px; top: 386px; width: 663px; height: 734px;
    background: #f9f9f9;
    border: 1px solid #cfcfcf;
    border-radius: 0 4px 4px 4px;
  }
  .card {
    background: var(--card);
    border: 1px solid #dcdcdc;
    border-radius: 5px;
    box-shadow: 0 1px 4px rgba(0,0,0,.12);
  }
  .intro-card { left: 55px; top: 409px; width: 621px; height: 223px; }
  .intro-title { left: 76px; top: 427px; font-size: 16px; color: #222; }
  .intro-copy {
    left: 71px; top: 455px; width: 600px;
    font-size: 12.4px; line-height: 16px; color: var(--muted);
  }

  .step {
    top: 516px; height: 84px;
    background: linear-gradient(#ececec, #ffffff 70%);
    border-radius: 5px 5px 0 0;
    text-align: center;
    font-size: 13px; color: #222;
    padding-top: 8px;
  }
  .step .icon {
    display: block; margin: 10px auto 0; width: 40px; height: 40px; border-radius: 8px;
  }

  .form-card { left: 52px; top: 659px; width: 624px; height: 435px; }
  .form-tab {
    left: 55px; top: 662px; width: 171px; height: 41px;
    background: linear-gradient(90deg, #ff7a12, #ffa94a);
    color: #fff; font-size: 16px;
    display: flex; align-items: center; padding-left: 40px;
  }
  .field-label { width: 160px; text-align: right; font-size: 13px; color: #555; }
  .field-input {
    left: 232px; width: 251px; height: 33px;
    background: #fff;
    border: 1px solid #c9c9c9; border-radius: 4px;
    font-size: 10px; color: var(--faint);
    display: flex; align-items: center; padding-left: 22px;
  }
  .field-hint { left: 232px; width: 246px; text-align: right; font-size: 9.5px; color: var(--faint); }
  .primary-btn {
    left: 249px; top: 1032px; width: 85px; height: 36px;
    background: linear-gradient(#ff8a3a, #e14a06);
    border: 2px solid #c9c9c9; border-radius: 6px;
    color: #fff; font-size: 12px; font-weight: 700;
    display: flex; align-items: center; justify-content: center;
  }

  /* message board */
  .message-board {
    left: 694px; top: 405px; width: 217px; height: 237px;
    background: linear-gradient(135deg, #ff9a2a, #f57a12 60%, #ff9a34);
    border-radius: 0 4px 4px 0;
    box-shadow: 0 1px 4px rgba(0,0,0,.2);
  }
  .board-title {
    left: 694px; top: 405px; width: 173px; height: 45px;
    background: linear-gradient(#ff8a1a, #ff9f3c);
    color: #fff; font-size: 16px;
    display: flex; align-items: center; padding-left: 30px;
  }
  .board-note {
    left: 715px; top: 474px; width: 160px; text-align: center;
    font-size: 10.5px; line-height: 16px; color: #3a1e00;
  }
  .board-input { left: 723px; top: 519px; width: 153px; height: 52px; background: #fff; border-radius: 5px; }
  .board-btn {
    left: 769px; top: 591px; width: 68px; height: 32px;
    background: linear-gradient(#ffffff, #e6e6e6);
    border-radius: 5px; font-size: 11px; color: #333;
    display: flex; align-items: center; justify-content: center;
  }

  .feedback-tab {
    left: 0; top: 579px; width: 55px; height: 172px;
    background: linear-gradient(90deg, #ffc23a, #ffa51a);
    border-radius: 0 6px 6px 0;
    box-shadow: 1px 1px 3px rgba(0,0,0,.2);
  }
  .feedback-tab span {
    position: absolute; left: 50%; top: 50%;
    transform: translate(-50%, -50%) rotate(-90deg);
    white-space: nowrap; font-size: 15px; color: #3a2400;
  }

  .footer { left: 0; top: 1162px; width: 924px; text-align: center; font-size: 12.5px; color: #333; }
</style>
</head>
<body>

  <div class="abs brand-name">BloomNest</div>
  <div class="abs user-bar"><span>Hi Sam Porter</span><span>|</span><span>Logout</span></div>

  <div class="abs header-band"></div>
  <div class="abs business-tab">Harbor Kites</div>

  <div class="abs logo-card">
    <span class="mark"></span>
    <span class="name">BloomNest</span>
  </div>

  <nav class="abs main-nav">
    <div class="nav-btn" style="left:31px;top:16px;">
      <svg viewBox="0 0 20 20"><circle cx="10" cy="10" r="8" fill="none" stroke="#fff" stroke-width="1.8"/><path d="M6 10.5l2.8 2.6L14 7.6" fill="none" stroke="#fff" stroke-width="1.8"/></svg>Dash Board</div>
    <div class="nav-btn" style="left:234px;top:16px;">
      <svg viewBox="0 0 20 20"><circle cx="10" cy="10" r="8" fill="none" stroke="#fff" stroke-width="1.8"/><path d="M6 10.5l2.8 2.6L14 7.6" fill="none" stroke="#fff" stroke-width="1.8"/></svg>My Contacts</div>
    <div class="nav-btn" style="left:31px;top:73px;">
      <svg viewBox="0 0 20 20"><circle cx="10" cy="10" r="8" fill="none" stroke="#fff" stroke-width="1.8"/><path d="M6 10.5l2.8 2.6L14 7.6" fill="none" stroke="#fff" stroke-width="1.8"/></svg>Account</div>
    <div class="nav-btn" style="left:234px;top:73px;">
      <svg viewBox="0 0 20 20"><circle cx="10" cy="10" r="8" fill="none" stroke="#fff" stroke-width="1.8"/><path d="M6 10.5l2.8 2.6L14 7.6" fill="none" stroke="#fff" stroke-width="1.8"/></svg>Create Campaign</div>
  </nav>

  <div class="abs tab is-active" style="left:32px;">Build</div>
  <div class="abs tab" style="left:162px;">Manage</div>
  <div class="abs tab" style="left:292px;">Mesure</div>
  <div class="abs tab" style="left:423px;">Share</div>

  <section class="abs workflow-panel"></section>

  <div class="abs card intro-card"></div>
  <h1 class="abs intro-title" style="font-weight:400;">Build: Start a Campaign or new activity</h1>
  <p class="abs intro-copy">Lorem ipsum dolor sit amet, consectetuer adipiscing elit. Nam nibh. Nunc varius facilisis eros. Sed erat. In in velit quis arcu ornare laoreet.Lorem ipsum dolor sit amet, consectetuer adipiscing elit. Nam nibh. Nunc varius facilisis eros. Sed erat. In in velit quis arcu ornare laoreet.</p>

  <div class="abs step" style="left:66px;width:105px;">Get Started
    <span class="icon" role="img" aria-label="Red start button icon with pointer" style="background:radial-gradient(circle,#e0262a 45%,#f4f4f4 47%);"></span></div>
  <div class="abs step" style="left:178px;width:113px;">Choose Template
    <span class="icon" role="img" aria-label="Template document icon" style="background:linear-gradient(135deg,#e9d9a8,#9db4d6);"></span></div>
  <div class="abs step" style="left:298px;width:105px;">Edit Email
    <span class="icon" role="img" aria-label="Yellow envelope with pencil icon" style="background:linear-gradient(135deg,#ffe15a,#f2b51a);"></span></div>
  <div class="abs step" style="left:410px;width:142px;">Select your send to list
    <span class="icon" role="img" aria-label="Grey and green exchange arrows icon" style="background:linear-gradient(#c9c9c9,#4fb33a);"></span></div>
  <div class="abs step" style="left:559px;width:105px;">Schedule
    <span class="icon" role="img" aria-label="Green calendar page icon" style="background:linear-gradient(#3aa843 0 25%,#f5f5f5 25%);"></span></div>

  <div class="abs card form-card"></div>
  <div class="abs form-tab">Form Field</div>

  <label class="abs field-label" style="left:52px;top:741px;">Name this Email:</label>
  <div class="abs field-input" style="top:730px;">Monthly Newsletter</div>
  <div class="abs field-hint" style="top:769px;">So you can track it in BloomNest</div>

  <label class="abs field-label" style="left:45px;top:816px;">Subject&nbsp;&nbsp;:</label>
  <div class="abs field-input" style="top:805px;">Small Businedd Tips</div>
  <div class="abs field-hint" style="top:845px;left:227px;">The Subject line for this Email</div>

  <label class="abs field-label" style="left:41px;top:889px;">Form&nbsp;&nbsp;&nbsp;:</label>
  <div class="abs field-input" style="top:880px;">BloomNest</div>
  <div class="abs field-hint" style="top:918px;left:233px;">The name receipients see in their mailbox</div>

  <label class="abs field-label" style="left:33px;top:963px;">Reply Email&nbsp;&nbsp;:</label>
  <div class="abs field-input" style="top:955px;">info@bloomnest-example.com</div>
  <div class="abs field-hint" style="top:993px;left:229px;">The email address recipients can respond to</div>

  <div class="abs primary-btn">Get Start</div>

  <aside class="abs message-board"></aside>
  <div class="abs board-title">Message Board</div>
  <p class="abs board-note">Sam,the social media leads are really coming in strong!</p>
  <div class="abs board-input"></div>
  <div class="abs board-btn">Add</div>

  <div class="abs feedback-tab"><span>Feed Back</span></div>

  <footer class="abs footer">Copyright 2011 BloomNest, All Rights Reserved</footer>

</body>
</html>
```